Need 8.5" x 11" as well as large 11"x17" Posters for our upcoming eventPlease include LOGOs in poster Main logo is Interfaith Youth Council of OCInfo/Content to include:All high school age faith groups are invited to come and join with 150 to 175 other high school students from various faith traditions to participate in the Crossways Teen Assembly of Lark Valley‘s Annual Crossways Teen Roundtable. More than ever, our county and the world needs young leaders who are willing to learn from each other and build stronger communities!FAITH FORUMThe purpose of this Crossways Teen Roundtable is to bring together young people from diverse ethnic, cultural, and religious backgrounds, and to engage them in dialogue. True dialogue is a conversation on a common subject between two or more persons of differing points of view and/or backgrounds. We feel that this commitment to dialogue will affect relationships in a constructive way in our places of worship and in our community.The forum itself involves having eight religiously diverse high school-age students, one adult, and youth leader around each table to discuss common questions. Our youth leaders act as facilitators, but it is stressed that it is the students we want to hear from.
Registration is Required for our BELIEF CIRCLE before February 25th, 2019
FORUM QUESTIONS and rregistration available online at http://ctalv.example/home/belief-fair/

Target Market(s)

Houses of worship, community leaders, High School Students

Industry/Entity Type

Non-Profit

Font styles to use
Serif

Colors
fefcec
f78f20
faa54b
fece3e
3176b5
33a6d7
0592cd
0455a3
f68d4d

Requirements
Must have
• Must Have:
• - Crossways Teen Assembly of Lark Valley's 15th Annual Belief Circle & Fair
• - TEENS EXPRESSING THEIR FAITH THROUGH ART, MUSIC, AND DIALOGUE
• - THIS YEAR'S THEME: "Rivers of Trust"
• - Sunday, March 10th, 2019 1:30pm-6:30pm
• - The Chapel of Harmon Grove Community Fellowship
• - 4817 Mellow Ridge Lane Dunmore Point, CA 93814
• - Email: ctalvorg@brightpost.example
• - Website: CTALV.example
• - Socialpage: Crossways Teen Assembly of Lark Valley
• Please include pictures provided
• Logo must be on there and prominent: Crossways Teen assembly of Lark Valley
• second logo should be somewhere on the bottom or back: Tall Harbor Allies
Nice to have
• Descriptions provided in word doc
• Ideally would like Logo and pictures and main info on the front
• - Website: CTALV.example
• On the back have more details about the program and pics if needed

```html
<!DOCTYPE html>
<html lang="en">
<head>
<meta charset="utf-8">
<title>Crossways Teen Assembly of Lark Valley – 15th Annual Belief Circle &amp; Fair</title>
<link rel="stylesheet" href="https://fonts.googleapis.com/css2?family=Bebas+Neue&family=Great+Vibes&family=Lato:wght@400;700&family=Libre+Baskerville:wght@400;700&family=Lobster&display=swap">
<style>
  :root {
    --orange: #f78f20;
    --orange-deep: #e9690c;
    --orange-light: #faa54b;
    --gold: #d9a520;
    --gold-light: #fece3e;
    --navy: #14173f;
    --ink: #1b1b1b;
    --charcoal: #2a2a2a;
    --cream: #fefcec;
    --white: #ffffff;
  }
  * { box-sizing: border-box; margin: 0; padding: 0; }
  html, body { width: 902px; height: 1200px; overflow: hidden; background: #ffffff; }
  .poster { position: relative; width: 902px; height: 1200px; overflow: hidden; background: #fff; }
  .art { position: absolute; inset: 0; }

  .org-logo {
    position: absolute; left: 112px; top: 60px; width: 236px; height: 236px;
    border: 3px solid var(--ink); border-radius: 50%;
    display: flex; align-items: center; justify-content: center; text-align: center;
    font-family: "Libre Baskerville", serif; font-weight: 700; font-size: 19px; line-height: 1.4;
    color: var(--ink); padding: 26px; background: rgba(255,255,255,0.85);
  }

  .event-host {
    position: absolute; left: 420px; top: 44px; width: 460px; text-align: center;
    font-family: "Lobster", cursive; font-weight: 400; font-size: 32px; line-height: 40px; color: var(--ink);
  }

  .anniversary {
    position: absolute; left: 579px; top: 138px; width: 140px; height: 140px; border-radius: 50%;
    background: radial-gradient(circle, #3a150e 0%, #1a0806 58%, #c8901a 74%, #fece3e 90%, #d9a520 100%);
  }
  .anniversary-text {
    position: absolute; left: 579px; top: 158px; width: 140px; text-align: center;
    font-family: "Great Vibes", cursive; color: var(--white); line-height: 1;
  }
  .anniversary-number { display: block; font-size: 54px; }
  .anniversary-word { display: block; font-size: 26px; margin-top: 2px; }

  .event-name {
    position: absolute; left: 420px; top: 290px; width: 460px; text-align: center;
    font-family: "Lobster", cursive; font-weight: 400; font-size: 32px; line-height: 40px; color: var(--ink);
  }
  .event-date {
    position: absolute; left: 385px; top: 339px; width: 492px; height: 44px;
    border-radius: 12px; background: linear-gradient(var(--orange-light), var(--orange-deep));
    border: 2px solid var(--navy);
    display: flex; align-items: center; justify-content: center;
    font-family: "Libre Baskerville", serif; font-weight: 700; font-size: 23px; color: var(--white);
  }
  .event-time {
    position: absolute; left: 507px; top: 397px; width: 244px; height: 36px;
    border-radius: 10px; background: var(--navy);
    display: flex; align-items: center; justify-content: center;
    font-family: "Libre Baskerville", serif; font-weight: 700; font-size: 20px; color: var(--white);
  }
  .divider-mark {
    position: absolute; left: 615px; width: 40px; height: 10px; border-radius: 5px;
    background: linear-gradient(90deg, var(--gold), var(--gold-light), var(--gold));
  }
  .venue, .address {
    position: absolute; left: 420px; width: 460px; text-align: center;
    font-family: "Libre Baskerville", serif; font-size: 21px; line-height: 1.4; color: var(--ink);
  }
  .venue { top: 486px; }
  .address { top: 594px; }

  .tagline {
    position: absolute; left: 0; top: 864px; width: 902px; text-align: center;
    font-family: "Bebas Neue", sans-serif; font-size: 56px; line-height: 62px; color: var(--ink);
  }
  .theme {
    position: absolute; left: 39px; top: 1002px; width: 825px; height: 40px; border-radius: 12px;
    background: linear-gradient(#f4f4f4, #bcbcbc 55%, #8d8d8d);
    border: 2px solid #555;
    display: flex; align-items: center; justify-content: center;
    font-family: "Libre Baskerville", serif; font-size: 23px; color: #333;
  }

  .contact { position: absolute; font-family: "Libre Baskerville", serif; color: var(--white); }
  .contact-web { left: 82px; top: 1111px; font-size: 20px; font-weight: 700; }
  .contact-mail { left: 82px; top: 1141px; font-size: 17px; }
  .footer-rule { position: absolute; left: 347px; top: 1108px; width: 1px; height: 76px; background: #555; }
  .social { position: absolute; left: 398px; top: 1124px; display: flex; align-items: center; gap: 12px;
    font-family: "Lato", sans-serif; font-size: 17px; color: var(--white); }
  .social-square { width: 30px; height: 30px; background: #3b5a99; border-radius: 2px; }
</style>
</head>
<body>
<main class="poster">
  <svg class="art" width="902" height="1200" viewBox="0 0 902 1200">
    <defs>
      <linearGradient id="page-bg" x1="0" y1="0" x2="0" y2="1">
        <stop offset="0" stop-color="#ffffff"/>
        <stop offset="0.3" stop-color="#f1f1f1"/>
        <stop offset="1" stop-color="#e6e3df"/>
      </linearGradient>
      <linearGradient id="crowd-tone" x1="0" y1="0" x2="0" y2="1">
        <stop offset="0" stop-color="#ffffff" stop-opacity="0"/>
        <stop offset="0.12" stop-color="#d9cdc6" stop-opacity="0.7"/>
        <stop offset="1" stop-color="#cfc6c3" stop-opacity="0.8"/>
      </linearGradient>
      <linearGradient id="orange-field" x1="0" y1="0" x2="0" y2="1">
        <stop offset="0" stop-color="#f68d4d"/>
        <stop offset="0.5" stop-color="#f78f20"/>
        <stop offset="1" stop-color="#faa54b"/>
      </linearGradient>
      <linearGradient id="gold-ring" x1="0" y1="0" x2="1" y2="1">
        <stop offset="0" stop-color="#fece3e"/>
        <stop offset="0.5" stop-color="#c8901a"/>
        <stop offset="1" stop-color="#fece3e"/>
      </linearGradient>
    </defs>

    <rect width="902" height="1200" fill="url(#page-bg)"/>
    <rect x="0" y="270" width="902" height="520" fill="url(#crowd-tone)" role="img" aria-label="Faded photo of a large group of teens seated at a previous forum"/>

    <path d="M0 555 C 220 640, 560 700, 902 730 L 902 1200 L 0 1200 Z" fill="url(#orange-field)"/>
    <path d="M560 700 C 700 715, 800 724, 902 730" fill="none" stroke="#14173f" stroke-width="4"/>

    <path d="M0 1085 C 300 1050, 600 1070, 902 1035 L 902 1200 L 0 1200 Z" fill="#ffffff"/>
    <path d="M0 1100 C 300 1068, 600 1088, 902 1052 L 902 1200 L 0 1200 Z" fill="#2a2a2a"/>

    <g stroke="url(#gold-ring)" stroke-width="6">
      <ellipse cx="181" cy="449" rx="180" ry="118" fill="#b79a8e" role="img" aria-label="Photo of students in dialogue around a round table"/>
      <ellipse cx="188" cy="676" rx="155" ry="91" fill="#a08a74" role="img" aria-label="Photo of four teen volunteers posing outdoors"/>
      <ellipse cx="425" cy="752" rx="142" ry="85" fill="#8d6f63" role="img" aria-label="Photo of teens performing music with traditional instruments"/>
      <ellipse cx="714" cy="757" rx="161" ry="85" fill="#a79a8c" role="img" aria-label="Photo of teens standing in a row holding candles"/>
    </g>

    <g fill="none" stroke="#ffffff" stroke-width="1.6">
      <circle cx="66" cy="1124" r="8"/>
      <ellipse cx="66" cy="1124" rx="3.5" ry="8"/>
      <line x1="58" y1="1124" x2="74" y2="1124"/>
      <rect x="59" y="1148" width="14" height="10"/>
      <polyline points="59,1148 66,1154 73,1148"/>
    </g>
  </svg>

  <div class="org-logo">Crossways Teen Assembly of Lark Valley</div>

  <h1 class="event-host">Crossways Teen Assembly<br>of Lark Valley's</h1>

  <div class="anniversary" role="img" aria-label="Gold anniversary medal with ribbon"></div>
  <p class="anniversary-text"><span class="anniversary-number">15th</span><span class="anniversary-word">Annual</span></p>

  <h2 class="event-name">Belief Circle &amp; Fair</h2>

  <p class="event-date">SUNDAY, MARCH 10TH, 2019</p>
  <p class="event-time">1:30PM-6:30PM</p>

  <span class="divider-mark" style="top:460px"></span>
  <p class="venue">The Chapel of Harmon Grove<br>Community Fellowship</p>
  <span class="divider-mark" style="top:566px"></span>
  <p class="address">4817 Mellow Ridge Lane<br>Dunmore Point, CA 93814</p>

  <p class="tagline">TEENS EXPRESSING THEIR FAITH THROUGH<br>ART, MUSIC, AND DIALOGUE</p>
  <p class="theme">THIS YEAR'S THEME: "RIVERS OF TRUST"</p>

  <p class="contact contact-web">www.CTALV.example</p>
  <p class="contact contact-mail">ctalvorg@brightpost.example</p>
  <span class="footer-rule"></span>
  <p class="social"><span class="social-square"></span>Socialpage: Crossways Teen Assembly of Lark Valley</p>
</main>
</body>
</html>
```